PowerPoint Listing Presentation for Real Estate Agency

We need a PowerPoint presentation for a new real estate brokerage team.

[[[[[[submit 1-3 sample slides for review - i will provide feedback and you can make changes if you want to - we will not be deciding on a design prior to the deadline]]]]]

******ATTN: DESIGNERS, if your skills are webdesign then just look at this like a portable website or a brochure. it should be easy enough******

NOTE: we have all the data to put into the slides. You just need to come up with the design and layout. we have a sample design that we like and have provided.

This focus will be for the home listing side of the business (a presentation for home sellers to convince them to use our services). The data and slides will present our team and the benefits, in the best light, to use our services over that of other real estate agent applying for the job. This presentation will proved facts and benefits and describe our special and unique offerings that will show a home seller why we can sell their home for more money in less time and with the least amount of hassle. The main color scheme is Dark Blue and White (we want some additional colors included - based on your creativity. otherwise the presentation will too monotone). We would like to see the use of Statistical Graphs (3-D) - data provided. We have photos of our team and a new logo (the logo could have some minor adjustment to clean it up if necessary) - also uploaded. We have about 80-90% of the information that will be put into the slides and will need to work closely to get the design and data integrated into the presentation (should be easier then it sounds). We should be able to add slides and data 'at will' over time via our master slides built into the presentation. We have a pretty good sample presentation that we like and can be used as a guideline (this is from our affiliated business network and we have full rights to all the information), it is uploaded but doesn't contain all the slide because of size limitations.

NOTE: An additional buyers presentation will be needed after we get the sellers presentation completed, which means additional work.

This should be enough to get you started and we are available if you have any questions to help you with the project. there will be around 60-70 total slides. once concept is completed it will be easy to create the slides.

Target Market(s)

home sellers. people who are moving to a new and better home or relocation for job reasons. typically more established in life

Industry/Entity Type

Real Estate

Requirements
Must have
• all the slides must be congruent. in other words, the exact same layout feel should used across the board. we are working on building our trade dress/image. Also, it must have a soft and inviting overall feel, yet show strength of ability.
Nice to have
• nice to have use of real people images when necessary. 3D graphs would be nice. clean modern look and feel, yet sophisticated and professional.
Should not have
• should not have a lot of time consuming transitions. do not include 3D stick figures or distracting moving gifs

```html
<!DOCTYPE html>
<html lang="en">
<head>
<meta charset="utf-8">
<title>Harlow &amp; Reed Team – Seller Listing Presentation</title>
<link rel="stylesheet" href="https://fonts.googleapis.com/css2?family=Tinos:wght@400;700&family=Open+Sans:wght@400;600;700&family=PT+Sans:wght@700&display=swap">
<style>
  :root{
    --stage:#ebe6de;
    --navy:#1c2a63;
    --blue:#1f8fd6;
    --blue-deep:#0f5fa8;
    --blue-light:#5fc1f0;
    --sky:#a9dcf6;
    --title-blue:#2a86c9;
    --ink:#333;
    --grey-text:#6b6b6b;
    --panel:#f2f3f5;
    --rule:#1c2a63;
    --red:#d23a3a;
    --green:#8cbf4a;
    --purple:#8e72b8;
  }
  *{box-sizing:border-box;margin:0;padding:0}
  html,body{width:1200px;height:648px;overflow:hidden;background:var(--stage)}
  .deck{position:relative;width:1200px;height:648px}
  .slide{position:absolute;width:308px;height:232px;overflow:hidden;background:linear-gradient(180deg,#fff 0%,#f1f2f4 100%);box-shadow:0 2px 6px rgba(0,0,0,.25);font-family:"Open Sans",sans-serif;color:var(--ink)}
  .s1{left:98px;top:64px}.s2{left:448px;top:63px}.s3{left:793px;top:63px}
  .s4{left:83px;top:354px}.s5{left:448px;top:354px}.s6{left:797px;top:354px}
  .slide--brand{background:linear-gradient(135deg,var(--blue-deep) 0%,var(--blue) 55%,var(--blue-light) 100%)}
  .backdrop{position:absolute;inset:0}
  .photo{position:absolute}
  .cover-title{position:absolute;left:8px;top:9px;font-family:"Tinos",serif;font-size:15.5px;line-height:19px;color:#fff}
  .wordmark-box{position:absolute;left:128px;top:183px;width:172px;height:40px;background:#fff;border:1px solid var(--navy);display:flex;align-items:center;justify-content:center}
  .wordmark{font-family:"Tinos",serif;font-size:17px;color:var(--navy);letter-spacing:.3px;white-space:nowrap}
  .pill{position:absolute;height:22px;border-radius:11px;background:linear-gradient(180deg,var(--blue-light),var(--blue-deep));box-shadow:0 2px 5px rgba(0,0,0,.45);color:#fff;font-family:"Tinos",serif;font-weight:700;display:flex;align-items:center;justify-content:center}
  .bullets{position:absolute;list-style:none}
  .bullets li{position:relative;padding-left:12px;margin-bottom:9px}
  .bullets li::before{content:"";position:absolute;left:0;top:2px;width:7px;height:7px;border-radius:50%;background:radial-gradient(circle at 35% 35%,var(--sky),var(--blue-deep))}
  .benefits{left:20px;top:40px;width:280px;font-size:7.6px;font-weight:700;line-height:10.5px}
  .reasons{left:16px;top:80px;width:286px;font-size:6.9px;line-height:9.3px;color:#444}
  .reasons li{margin-bottom:6.5px}
  .slide-title{position:absolute;left:16px;top:10px;font-family:"Tinos",serif;font-weight:700;font-size:12.5px;color:var(--title-blue);padding-bottom:1px;border-bottom:1.5px solid var(--rule);white-space:nowrap}
  .s4 .slide-title,.s5 .slide-title{left:21px}
  .reasons-pill{left:14px;top:30px;width:178px;height:30px;border-radius:15px;flex-direction:column;align-items:flex-start;padding-left:10px}
  .reasons-pill strong{font-size:12px;line-height:13px}
  .reasons-pill small{font-size:5px;line-height:7px;font-weight:700}
  .reasons-count{position:absolute;left:168px;top:33px;width:26px;height:26px;border-radius:50%;background:#fff;border:2px solid var(--blue-deep);font-family:"Tinos",serif;font-weight:700;font-size:17px;color:var(--navy);display:flex;align-items:center;justify-content:center}
  .lead{position:absolute;left:21px;top:33px;width:270px;font-size:8.2px;line-height:12px;color:var(--grey-text)}
  .promo{position:absolute;left:0;top:76px;width:309px;height:156px;background:linear-gradient(90deg,#c9ced6 0%,#9aa3b0 55%,#7d8796 100%)}
  .promo-headline{position:absolute;right:10px;top:18px;text-align:right;color:#fff;font-family:"PT Sans",sans-serif;font-weight:700;font-size:24px;line-height:26px;text-shadow:0 1px 2px rgba(0,0,0,.3)}
  .promo-sub{position:absolute;right:10px;top:75px;text-align:right;color:#fff;font-family:"Open Sans",sans-serif;font-size:11px;line-height:13px}
  .stat-panel{position:absolute;left:20px;top:84px;width:138px;height:130px;border-radius:10px;background:var(--panel);box-shadow:inset 0 0 0 1px #dde0e4}
  .stat-pill{left:22px;top:77px;width:136px;height:20px;font-size:9px}
  .stat-line{position:absolute;left:30px;font-size:7.2px;color:var(--grey-text)}
  .chart{position:absolute}
  .chart text{font-family:"Open Sans",sans-serif}
  .thanks{position:absolute;left:148px;top:188px;width:150px;text-align:center;font-family:"Tinos",serif;font-size:27px;color:var(--navy)}
  .end-mark{position:absolute;left:174px;top:120px;width:98px;text-align:center;font-family:"Tinos",serif;font-size:15px;color:var(--navy);line-height:18px}
</style>
</head>
<body>
<main class="deck">

  <!-- Cover -->
  <section class="slide slide--brand s1">
    <svg class="backdrop" viewBox="0 0 308 232" aria-hidden="true">
      <circle cx="298" cy="180" r="138" fill="none" stroke="var(--sky)" stroke-width="5" opacity=".6"/>
      <circle cx="298" cy="180" r="128" fill="#fff"/>
    </svg>
    <div class="photo" role="img" aria-label="Two open hands forming a roof over a small blue model house" style="left:178px;top:58px;width:126px;height:120px;border-radius:50% 0 0 50%;background:radial-gradient(circle at 55% 55%,#2b8fd4 0%,#7fbde6 30%,#f1ddd0 60%,#fff 90%)"></div>
    <div class="photo" role="img" aria-label="Smiling family of four sitting together" style="left:2px;top:148px;width:110px;height:84px;background:linear-gradient(90deg,rgba(210,225,240,.65),rgba(170,205,235,.35));border-radius:30px 30px 0 0"></div>
    <h1 class="cover-title">The Harlow &amp; Reed Team<br>Helping You Home</h1>
    <div class="wordmark-box"><span class="wordmark">HARLOW &amp; REED</span></div>
  </section>

  <!-- Benefits -->
  <section class="slide s2">
    <div class="pill" style="left:14px;top:10px;width:150px;font-size:11px">Our VIP Seller Benefits</div>
    <ul class="bullets benefits">
      <li>Your Home Sold at a Price Acceptable to You (Guaranteed in Writing) or We’ll Buy it for Cash!</li>
      <li>Buy Any One of Our Listings and if YOU Are Not Satisfied in 24 Months WE’LL BUY IT BACK!</li>
    </ul>
    <div class="photo" role="img" aria-label="Portrait of the two team agents in dark suits" style="left:86px;top:92px;width:222px;height:140px;background:linear-gradient(180deg,#eef0f2 0%,#d9dde2 40%,#2b2f38 75%,#1d2028 100%)"></div>
  </section>

  <!-- Reasons -->
  <section class="slide s3">
    <h2 class="slide-title">The Harlow &amp; Reed Team’s Success Can Be Yours</h2>
    <div class="pill reasons-pill"><strong>The Biggest Reasons</strong><small>for The Harlow &amp; Reed Team to Sell Your Home</small></div>
    <div class="reasons-count">5</div>
    <ul class="bullets reasons">
      <li>We Sell More Homes: you get more experience which ensures smooth transactions and no hassles.</li>
      <li>We Sell for Top Dollar: our negotiating experience and target marketing will make sure you get the most for your home.</li>
      <li>We Will Get Your Home Sold: we sell the homes we list; we have an amazing success rate of 98%.</li>
      <li>Our Track Record: over 90% of our clients keep coming back to The Harlow &amp; Reed Team for the next real estate transaction, plus you’re protected with our 5 star guarantee.</li>
      <li>Guaranteed Sale &amp; Trade Up Program: you won’t be stuck paying you mortgages or have to deal with conditional sale offers.</li>
    </ul>
  </section>

  <!-- Trade up -->
  <section class="slide s4">
    <h2 class="slide-title">Guaranteed Sale &amp; Trade Up Program</h2>
    <p class="lead">You won’t be stuck paying you mortgages or have to deal with conditional sale offers.</p>
    <div class="promo">
      <div class="photo" role="img" aria-label="Model house resting on a large golden key and coins" style="left:18px;top:22px;width:120px;height:124px;background:radial-gradient(ellipse at 50% 60%,#e9eef5 0%,#c9b37a 45%,rgba(160,168,180,0) 75%)"></div>
      <div class="promo-headline">Insider Secrets<br>Revealed</div>
      <div class="promo-sub">..a must-read for<br>Home-Owners &amp; Renters!</div>
    </div>
  </section>

  <!-- Graph -->
  <section class="slide s5">
    <h2 class="slide-title">Graph</h2>
    <p class="lead">The Harlow &amp; Reed Team SOLD 18 Times More Homes Then the Average Agent!</p>
    <div class="stat-panel"></div>
    <div class="pill stat-pill">End-buyers</div>
    <p class="stat-line" style="top:103px">Number of Homes Sold in 2012 = 55</p>
    <p class="stat-line" style="top:120px">Average Agent = &lt;3</p>
    <svg class="chart" style="left:26px;top:150px" width="118" height="60" viewBox="0 0 118 60" aria-label="Homes sold by age group, 2011 and 2012">
      <rect width="118" height="60" fill="#fff"/>
      <g font-size="3.2" fill="#555">
        <text x="1" y="7">70+</text><text x="1" y="13">60-69</text><text x="1" y="19">50-59</text><text x="1" y="25">40-49</text><text x="1" y="31">30-39</text><text x="1" y="37">20-29</text><text x="1" y="43">10-19</text><text x="1" y="49">0-9</text>
      </g>
      <g fill="var(--navy)">
        <rect x="12" y="4" width="52" height="2"/><rect x="12" y="10" width="60" height="2"/><rect x="12" y="16" width="66" height="2"/><rect x="12" y="22" width="70" height="2"/><rect x="12" y="28" width="74" height="2"/><rect x="12" y="34" width="78" height="2"/><rect x="12" y="40" width="80" height="2"/><rect x="12" y="46" width="82" height="2"/>
      </g>
      <g fill="var(--red)">
        <rect x="12" y="6.3" width="40" height="1.6"/><rect x="12" y="12.3" width="48" height="1.6"/><rect x="12" y="18.3" width="52" height="1.6"/><rect x="12" y="24.3" width="58" height="1.6"/><rect x="12" y="30.3" width="62" height="1.6"/><rect x="12" y="36.3" width="66" height="1.6"/><rect x="12" y="42.3" width="70" height="1.6"/><rect x="12" y="48.3" width="72" height="1.6"/>
      </g>
      <g font-size="3" fill="#555"><rect x="76" y="6" width="3" height="2" fill="var(--red)"/><text x="80" y="8">2011</text><rect x="76" y="10" width="3" height="2" fill="var(--navy)"/><text x="80" y="12">2012</text></g>
      <g font-size="3" fill="#555"><text x="12" y="56">0</text><text x="36" y="56">10</text><text x="60" y="56">20</text><text x="84" y="56">30</text><text x="106" y="56">40</text></g>
    </svg>
    <svg class="chart" style="left:180px;top:96px" width="100" height="62" viewBox="0 0 100 62" aria-label="Sales growth columns with market rate line">
      <rect width="100" height="62" fill="#fff"/>
      <g font-size="3" fill="#555"><text x="1" y="6">10%</text><text x="1" y="16">8%</text><text x="1" y="26">6%</text><text x="1" y="36">4%</text><text x="1" y="46">2%</text><text x="1" y="54">0%</text></g>
      <g fill="var(--blue-deep)">
        <rect x="12" y="30" width="4" height="22"/><rect x="20" y="26" width="4" height="26"/><rect x="28" y="28" width="4" height="24"/><rect x="36" y="29" width="4" height="23"/><rect x="44" y="32" width="4" height="20"/><rect x="52" y="31" width="4" height="21"/><rect x="60" y="20" width="4" height="32"/><rect x="68" y="30" width="4" height="22"/><rect x="76" y="28" width="4" height="24"/>
      </g>
      <polyline points="14,8 22,9 30,10 38,11 46,13 54,16 62,18 70,22 78,24" fill="none" stroke="var(--red)" stroke-width="1.2"/>
      <line x1="11" y1="52" x2="84" y2="52" stroke="#999" stroke-width=".4"/>
      <g font-size="3" fill="#555"><rect x="56" y="2" width="5" height="1.6" fill="var(--blue-deep)"/><text x="62" y="4">Sales Growth</text><rect x="56" y="6" width="5" height="1" fill="var(--red)"/><text x="62" y="8">Market Rate</text></g>
      <g font-size="2.8" fill="#555"><text x="11" y="58">06</text><text x="19" y="58">07</text><text x="27" y="58">08</text><text x="35" y="58">09</text><text x="43" y="58">10</text><text x="51" y="58">11</text><text x="59" y="58">12</text><text x="67" y="58">13</text><text x="75" y="58">14</text></g>
    </svg>
    <svg class="chart" style="left:180px;top:166px" width="110" height="58" viewBox="0 0 110 58" aria-label="Homes by household income, stacked columns">
      <rect width="110" height="58" fill="#fff"/>
      <text x="20" y="5" font-size="3.2" fill="#333" font-weight="700">Homes by household income</text>
      <g font-size="3" fill="#555"><text x="1" y="12">200</text><text x="1" y="23">150</text><text x="1" y="34">100</text><text x="1" y="45">50</text><text x="1" y="54">0</text></g>
      <g>
        <rect x="14" y="40" width="6" height="12" fill="var(--blue-deep)"/><rect x="14" y="30" width="6" height="10" fill="var(--red)"/><rect x="14" y="20" width="6" height="10" fill="var(--green)"/><rect x="14" y="14" width="6" height="6" fill="var(--purple)"/>
        <rect x="28" y="42" width="6" height="10" fill="var(--blue-deep)"/><rect x="28" y="28" width="6" height="14" fill="var(--red)"/><rect x="28" y="18" width="6" height="10" fill="var(--green)"/><rect x="28" y="12" width="6" height="6" fill="var(--purple)"/>
        <rect x="42" y="44" width="6" height="8" fill="var(--blue-deep)"/><rect x="42" y="32" width="6" height="12" fill="var(--red)"/><rect x="42" y="22" width="6" height="10" fill="var(--green)"/><rect x="42" y="16" width="6" height="6" fill="var(--purple)"/>
        <rect x="56" y="42" width="6" height="10" fill="var(--blue-deep)"/><rect x="56" y="26" width="6" height="16" fill="var(--red)"/><rect x="56" y="16" width="6" height="10" fill="var(--green)"/><rect x="56" y="10" width="6" height="6" fill="var(--purple)"/>
      </g>
      <g font-size="3" fill="#555">
        <rect x="70" y="12" width="3" height="2" fill="var(--purple)"/><text x="74" y="14">Class A</text>
        <rect x="70" y="20" width="3" height="2" fill="var(--green)"/><text x="74" y="22">Class B</text>
        <rect x="70" y="28" width="3" height="2" fill="var(--red)"/><text x="74" y="30">Class C</text>
        <rect x="70" y="36" width="3" height="2" fill="var(--blue-deep)"/><text x="74" y="38">Class D</text>
      </g>
    </svg>
  </section>

  <!-- Closing -->
  <section class="slide slide--brand s6">
    <svg class="backdrop" viewBox="0 0 308 232" aria-hidden="true">
      <circle cx="300" cy="175" r="140" fill="none" stroke="var(--sky)" stroke-width="5" opacity=".6"/>
      <circle cx="300" cy="175" r="130" fill="#fff"/>
    </svg>
    <div class="photo" role="img" aria-label="Smiling family of four sitting together" style="left:2px;top:148px;width:110px;height:84px;background:linear-gradient(90deg,rgba(210,225,240,.65),rgba(170,205,235,.35));border-radius:30px 30px 0 0"></div>
    <div class="end-mark">HARLOW &amp; REED</div>
    <p class="thanks">Thank You!</p>
  </section>

</main>
</body>
</html>
```